900mm double sided Card Ponytail Insert for hair

I need print ready file designs for card packaging inserts for my line of ponytails, These are two sided colour and fold at each end or contain the hair, for structure and so the brand is on display. These will be marketed as luxury ponytails, so we want a simple, soft but luxurious design feel. All the details are below but it will be the logo, photos and simple messaging

Target Market(s)

18-30 females

Industry/Entity Type

Beauty

Font styles to use
Serif

Requirements
Must have
• - Lumera Logo on the back and top front fold.
'Luxury Synthetic Ponytails' Head line
'For effortlessly long and luxurious hair' tag line
'For tutorials, questions and inspiration head to our 'Brightroom' on lumerabeauty.com'
www.lumerabeauty.com
Tag us on socials! @lumerabeautyofficial (pictavo and Chatterloop logos)
3 step-by-step pictures (holding pictures please until i have some taken)
Nice to have
• (notes to designers) view our website to see our branding lumerabeauty.com - it would be good to use our brand colours and somekind of tropical leaves maybe? i'm thinking palm leaves?
- my brand font is Sweet Getaway - but this may only be good for the biggest headings

```html
<!DOCTYPE html>
<html lang="en">
<head>
<meta charset="utf-8">
<title>Lumera Ponytail Insert</title>
<link rel="stylesheet" href="https://fonts.googleapis.com/css2?family=Oswald:wght@500&family=Playfair+Display:wght@600&family=Cormorant+Garamond:wght@500;600&display=swap">
<style>
:root{
  --page:#ffffff;
  --board:#cfd0d2;
  --cream:#fbf5ea;
  --pink:#e8407e;
  --teal:#4cc2b0;
  --teal-soft:#8fdccf;
  --teal-deep:#2f9f92;
  --gold:#d9b15c;
  --gold-light:#f1d9a0;
  --ink:#5a5a5a;
  --photo:#d8c3aa;
  --photo-dark:#b89675;
  --fold:#9a9a9a;
}
*{margin:0;padding:0;box-sizing:border-box}
html,body{width:793px;height:1200px;overflow:hidden;background:var(--page)}
.canvas{position:relative;width:793px;height:1200px;background:var(--page)}
.board{position:absolute;left:87px;top:0;width:528px;height:1200px;background:var(--board)}
.strip{position:absolute;background:var(--cream);overflow:hidden;box-shadow:0 0 3px rgba(0,0,0,.12)}
.strip-front{left:185px;top:66px;width:100px;height:1043px}
.strip-back{left:412px;top:232px;width:105px;height:811px}
.fold-line{position:absolute;height:1px;background:var(--fold)}
.abs{position:absolute}
.logo{text-align:center;font-family:"Playfair Display",serif;font-weight:600;color:var(--teal);}
.logo .dot{display:inline-block;width:7px;height:7px;border-radius:50%;background:var(--teal);margin-right:3px;vertical-align:middle}
.headline{font-family:"Oswald",sans-serif;font-weight:500;color:var(--pink);text-align:center;letter-spacing:.5px;line-height:1.15}
.body{font-family:"Cormorant Garamond",serif;font-weight:600;text-align:center;line-height:1.2}
.teal{color:var(--teal-deep)}
.pink{color:var(--pink)}
.photo{position:absolute;background:linear-gradient(160deg,var(--photo),var(--photo-dark));border-radius:2px}
.pill{position:absolute;border-radius:8px;text-align:center;font-family:"Oswald",sans-serif;font-size:6px;color:#fff;letter-spacing:.5px}
.pill-teal{background:var(--teal)}
.pill-gold{background:linear-gradient(90deg,var(--gold),var(--gold-light),var(--gold))}
.step{position:absolute;width:40px;font-size:6.5px}
.flip{position:absolute;left:0;top:0;width:100px;height:140px;transform:rotate(180deg)}
.social{display:inline-block;width:7px;height:7px;border-radius:50%;background:var(--teal);margin:0 1px}
.tropical{position:absolute;left:0;top:150px;width:105px;height:590px;background:radial-gradient(circle at 40% 30%,var(--teal-soft),var(--teal) 60%,var(--teal-deep))}
</style>
</head>
<body>
<div class="canvas">
  <div class="board"></div>

  <!-- front strip -->
  <div class="strip strip-front">
    <div class="flip">
      <svg class="abs" style="left:0;top:0" width="100" height="14" viewBox="0 0 100 14"><path d="M0 8 Q50 -4 100 8 V0 H0Z" fill="var(--gold)"/></svg>
      <div class="headline abs" style="left:8px;top:22px;width:84px;font-size:9px">LUXURY SYNTHETIC<br>PONYTAILS</div>
      <div class="body pink abs" style="left:10px;top:48px;width:80px;font-size:6px">For effortlessly long and luxurious hair</div>
      <div class="logo abs" style="left:0;top:80px;width:100px;font-size:15px"><span class="dot"></span>Lumera</div>
    </div>

    <div class="logo abs" style="left:0;top:175px;width:100px;font-size:18px"><span class="dot"></span>Lumera</div>
    <div class="body teal abs" style="left:8px;top:262px;width:84px;font-size:7px">For effortlessly long and luxurious hair</div>

    <div class="photo" role="img" aria-label="Model with ponytail, back view" style="left:10px;top:298px;width:36px;height:56px"></div>
    <div class="photo" role="img" aria-label="Model with ponytail, side view" style="left:54px;top:298px;width:36px;height:56px"></div>
    <div class="body teal abs" style="left:10px;top:357px;width:36px;font-size:6px">Before</div>
    <div class="body teal abs" style="left:54px;top:357px;width:36px;font-size:6px">After</div>

    <div class="pill pill-teal" style="left:22px;top:395px;width:56px;height:12px;line-height:12px">STEP BY STEP</div>

    <div class="photo" role="img" aria-label="Step one: gathering hair" style="left:10px;top:425px;width:40px;height:52px"></div>
    <div class="step body teal" style="left:54px;top:440px">Step 1 Gather hair high</div>

    <div class="step body teal" style="left:8px;top:510px">Step 2 Wrap and clip</div>
    <div class="photo" role="img" aria-label="Step two: attaching ponytail" style="left:50px;top:495px;width:40px;height:52px"></div>

    <div class="photo" role="img" aria-label="Step three: finished ponytail" style="left:10px;top:568px;width:40px;height:52px"></div>
    <div class="step body teal" style="left:54px;top:585px">Step 3 Smooth and style</div>

    <div class="photo" role="img" aria-label="Model showing curly ponytail" style="left:10px;top:640px;width:38px;height:60px"></div>
    <div class="photo" role="img" aria-label="Model showing finished look" style="left:52px;top:640px;width:38px;height:60px"></div>

    <div class="pill pill-gold" style="left:14px;top:712px;width:72px;height:11px;line-height:11px">Shop the full collection</div>

    <div class="photo" role="img" aria-label="Portrait of model with long wavy ponytail" style="left:14px;top:732px;width:72px;height:132px"></div>

    <div class="body teal abs" style="left:4px;top:878px;width:92px;font-size:6.5px">www.lumerabeauty.com</div>
    <div class="body teal abs" style="left:4px;top:890px;width:92px;font-size:5.5px">Tag us on socials! @lumerabeautyofficial</div>
    <div class="abs" style="left:0;top:906px;width:100px;text-align:center;font-family:'Cormorant Garamond',serif;font-size:5.5px;color:var(--teal-deep)"><span class="social"></span> pictavo <span class="social"></span> Chatterloop</div>

    <div class="body pink abs" style="left:8px;top:968px;width:84px;font-size:6px">For tutorials, questions and inspiration head to our 'Brightroom' on lumerabeauty.com</div>
    <svg class="abs" style="left:0;top:1026px" width="100" height="17" viewBox="0 0 100 17"><path d="M0 6 Q50 18 100 6 V17 H0Z" fill="var(--gold)"/></svg>
  </div>
  <div class="fold-line" style="left:172px;top:206px;width:126px"></div>
  <div class="fold-line" style="left:172px;top:211px;width:126px"></div>
  <div class="fold-line" style="left:172px;top:1003px;width:126px"></div>
  <div class="fold-line" style="left:172px;top:1010px;width:126px"></div>

  <!-- back strip -->
  <div class="strip strip-back">
    <div class="logo abs" style="left:0;top:26px;width:105px;font-size:18px"><span class="dot"></span>Lumera</div>
    <div class="headline abs" style="left:6px;top:82px;width:93px;font-size:10px">LUXURY SYNTHETIC<br>PONYTAILS</div>
    <div class="body pink abs" style="left:8px;top:112px;width:89px;font-size:5.5px">For effortlessly long and luxurious hair</div>
    <div class="tropical" role="img" aria-label="Soft teal background with palm leaves"></div>
    <svg class="abs" style="left:0;top:140px" width="105" height="22" viewBox="0 0 105 22"><path d="M0 20 Q50 0 105 10" stroke="var(--gold)" stroke-width="2.5" fill="none"/></svg>
    <svg class="abs" style="left:0;top:728px" width="105" height="22" viewBox="0 0 105 22"><path d="M0 12 Q55 22 105 2" stroke="var(--gold)" stroke-width="2.5" fill="none"/></svg>
    <div class="body pink abs" style="left:8px;top:752px;width:89px;font-size:5.5px">For tutorials, questions and inspiration head to our 'Brightroom'</div>
    <div class="pill pill-gold" style="left:14px;top:782px;width:77px;height:10px;line-height:10px;font-size:5.5px">www.lumerabeauty.com</div>
  </div>
</div>
</body>
</html>
```